Business Card/Logo Design Project

Design the Business card For a psychologist providing relationship workshops, see website draft at www.quietbridgeworks.com.au.

The background is to be beige with shadows in ivory of the letter "L" as shown on the website noted above.

The words "Kind Harbour" on the front with the first letter of each word in very scrolled lettering and the remaining letters more formal. The front design is to be the logo of the business for use on other items.

The reverse is to show...

client's name
date
time
workshop number
workshop name
and at the bottom "PLEASE BE PUNCTUAL. BRING NOTEPAD & PEN"

Target Market(s)

female, middle-class, educated, introspective

Industry/Entity Type

Business

Requirements
Must have
• see www.quietbridgeworks.com.au for the design aesthetic - just need you to make it look professional.

cream, beige, grey, chocolate, tan, ivory.

calligraphy shadows as per referenced website

business card back, flyer and postcard to just be background so that I can add text on top through printmarlow.

see website for colour-scheme.
Should not have
• not cutesy, pink, or mushy

```html
<!DOCTYPE html>
<html lang="en">
<head>
<meta charset="utf-8">
<title>Kind Harbour – Business Card</title>
<link rel="stylesheet" href="https://fonts.googleapis.com/css2?family=Tinos&family=Allura&display=swap">
<style>
  :root {
    --page: #ffffff;
    --card: #5e4635;
    --card-flourish: #735738;
    --ink: #f7e0d0;
    --card-shadow: rgba(0, 0, 0, 0.28);
  }
  * { margin: 0; padding: 0; box-sizing: border-box; }
  html, body {
    width: 1016px;
    height: 1200px;
    overflow: hidden;
    background: var(--page);
  }
  .sheet {
    position: relative;
    width: 1016px;
    height: 1200px;
  }
  .card {
    position: absolute;
    left: 116px;
    width: 793px;
    height: 447px;
    background: var(--card);
    box-shadow: 4px 8px 14px var(--card-shadow);
    overflow: hidden;
    color: var(--ink);
  }
  .card--front { top: 131px; }
  .card--back { top: 632px; left: 117px; }

  .flourish-shadow {
    position: absolute;
    inset: 0;
    background:
      radial-gradient(ellipse 38% 60% at 30% 45%, var(--card-flourish) 0%, rgba(115, 87, 56, 0) 70%),
      radial-gradient(ellipse 30% 45% at 85% 60%, var(--card-flourish) 0%, rgba(115, 87, 56, 0) 70%);
    opacity: 0.8;
  }

  .brand-name {
    position: absolute;
    left: 0;
    right: 0;
    top: 186px;
    text-align: center;
    font-family: "Tinos", serif;
    font-size: 78px;
    font-weight: 400;
    line-height: 1;
    letter-spacing: 1px;
    color: var(--ink);
  }
  .brand-domain {
    position: absolute;
    right: 72px;
    top: 262px;
    font-family: "Tinos", serif;
    font-size: 21px;
    color: var(--ink);
  }

  .back-title {
    position: absolute;
    left: 0;
    right: 0;
    top: 54px;
    text-align: center;
    font-family: "Allura", cursive;
    font-size: 54px;
    line-height: 1;
    color: var(--ink);
  }
  .field {
    position: absolute;
    display: flex;
    align-items: flex-end;
    font-family: "Tinos", serif;
    font-size: 22px;
    line-height: 1;
    color: var(--ink);
  }
  .field__rule {
    flex: 1;
    height: 2px;
    background: var(--ink);
    margin-left: 12px;
    margin-bottom: 1px;
  }
  .field--client { left: 41px; width: 703px; top: 147px; }
  .field--date { left: 41px; width: 339px; top: 205px; }
  .field--time { left: 416px; width: 328px; top: 205px; }
  .field--time .field__rule { margin-left: 26px; }
  .field--workshop { left: 41px; width: 703px; top: 264px; }
  .blank-rule {
    position: absolute;
    left: 41px;
    width: 703px;
    top: 336px;
    height: 2px;
    background: var(--ink);
  }
  .back-note {
    position: absolute;
    left: 0;
    right: 0;
    top: 380px;
    text-align: center;
    font-family: "Tinos", serif;
    font-size: 22px;
    color: var(--ink);
  }
</style>
</head>
<body>
<main class="sheet">
  <section class="card card--front">
    <div class="flourish-shadow" role="img" aria-label="Large faint calligraphic flourish shadows in tan across the card"></div>
    <h1 class="brand-name">Kind Harbour</h1>
    <span class="brand-domain">.com.au</span>
  </section>

  <section class="card card--back">
    <h2 class="back-title">Appointment / Workshop</h2>
    <div class="field field--client"><span>Client Name</span><span class="field__rule"></span></div>
    <div class="field field--date"><span>Date(s)</span><span class="field__rule"></span></div>
    <div class="field field--time"><span>Time</span><span class="field__rule"></span></div>
    <div class="field field--workshop"><span>Workshop No &amp; Name</span><span class="field__rule"></span></div>
    <div class="blank-rule"></div>
    <p class="back-note">Please be punctual. Bring a Notepad &amp; Pen.</p>
  </section>
</main>
</body>
</html>
```